Looking for a web design for event planning. Targeting the Wedding Industry, Corporate Meetings, Special Events, Fundraisers and other Celebratory Events
Home Page - name with pictures of various events- 3 buttons to go to
Wedding ( engagement parties, bridal showers, rehearsal dinners, welcome receptions and wedding receptions page
Corporate Meetings/Fundraisers page
Special Events/Celebratory Events
Updates

Target Market(s)

Brides, Wedding Planners, Corporate Event Planners, Destination Companies, Public

Industry/Entity Type

Event Planning

Contact Information for Business Card

name , phone number and email address
images of party images...wedding cake- balloons-party hat etc

Logo Text

Dana Ruth Okonkwo Event Design @ The Bayview Harbor Rowing Club

Number of Pages Required

4 page

Font styles to use
Decorative

Colors

Designer to choose colors to be used in the design.

Requirements
Must have
• Dana Ruth Okonkwo Event Design
• @ Bayview Harbor Rowing Club
• 415-555-0193
• droeventstudio@vesperlane.com
• back side of card - Image of Bayview Harbor Rowing Club
Nice to have
• fun and catchy party images
• wedding cake - diamond ring -balloons - party hat- flowers
• would like to see the images in white, gold and silver
Should not have
• photographic pictures

```html
<!DOCTYPE html>
<html lang="en">
<head>
<meta charset="utf-8">
<title>Dana Ruth Okonkwo Event Design</title>
<link rel="stylesheet" href="https://fonts.googleapis.com/css2?family=Source+Sans+3:wght@300;400;600;700;900&display=swap">
<style>
:root{
  --bg:#efefef;
  --orange:#f47b20;
  --amber:#f7a531;
  --ink:#222;
  --muted:#777;
  --soft:#f5f5f5;
  --footer:#15151f;
  --white:#fff;
}
*{box-sizing:border-box;margin:0;padding:0}
html,body{width:1200px;height:1200px;overflow:hidden;background:var(--bg);font-family:"Source Sans 3",sans-serif;color:var(--ink)}
.stage{position:absolute;left:0;top:0;width:1500px;height:1500px;transform:scale(.8);transform-origin:0 0}
.page{position:absolute;left:488px;top:0;width:526px;height:1500px;background:var(--white);overflow:hidden}
.abs{position:absolute}
.btn{position:absolute;border-radius:20px;font-size:4.5px;font-weight:600;display:flex;align-items:center;justify-content:center;letter-spacing:.2px;white-space:nowrap}
.btn-solid{background:linear-gradient(90deg,var(--orange),var(--amber));color:var(--white)}
.btn-line{border:1px solid var(--amber);color:var(--white)}
.btn-line-dark{border:1px solid var(--amber);color:var(--ink);background:var(--white)}

/* header */
.hero-photo{left:0;top:0;width:526px;height:360px;background:
  radial-gradient(ellipse 120px 90px at 300px 140px,rgba(214,170,140,.55),transparent 70%),
  radial-gradient(ellipse 90px 80px at 110px 150px,rgba(200,150,120,.45),transparent 70%),
  radial-gradient(ellipse 90px 90px at 440px 170px,rgba(190,150,130,.45),transparent 70%),
  linear-gradient(160deg,#4a3e4a 0%,#3a2d35 40%,#5e4638 70%,#2e2630 100%)}
.brand{left:65px;top:21px;font-size:7.5px;font-weight:700;line-height:1;color:#333;white-space:nowrap}
.call{left:177px;top:18px;border-left:1px solid #333;padding-left:5px}
.call small{display:block;font-size:4px;color:var(--orange)}
.call span{font-size:6px;color:#222}
.nav{left:248px;top:71px;display:flex;align-items:center;font-size:5px;color:var(--white)}
.nav a{margin-right:17px}
.nav .pill{border:1px solid var(--white);border-radius:10px;padding:2px 4px;font-size:4px}
.hero-text{left:0;width:526px;top:176px;text-align:center;color:var(--white)}
.hero-text .l1{font-size:17px;font-weight:300;letter-spacing:.5px;line-height:1}
.hero-text .l2{font-size:21px;font-weight:700;line-height:1.1}

/* welcome */
.welcome{left:0;top:360px;width:526px;height:191px;background:var(--soft)}
.w-kicker{left:65px;top:35px;font-size:9px;font-weight:400;color:#555}
.w-title{left:65px;top:49px;font-size:9.5px;font-weight:600;color:#222}
.w-copy{left:65px;top:70px;width:180px;font-size:4.3px;line-height:7.6px;color:#444}
.features{left:278px;top:19px;width:165px;height:143px;display:grid;grid-template-columns:1fr 1fr;gap:1px;background:#eee}
.feature{background:var(--white);text-align:center;padding-top:10px}
.feature svg{width:20px;height:20px}
.feature h4{font-size:6px;font-weight:600;margin-top:2px}
.feature p{font-size:4px;color:var(--muted);line-height:7px;margin:2px 14px 0}

/* video band */
.band{left:0;top:551px;width:526px;height:148px}
.band-photo{left:0;top:0;width:526px;height:129px;background:
  radial-gradient(ellipse 50px 70px at 355px 70px,rgba(235,225,215,.55),transparent 70%),
  linear-gradient(90deg,#2a2a33 0%,#3a3640 30%,#5a4a44 55%,#6a5646 75%,#3b3530 100%)}
.band-title{left:65px;top:40px;font-size:10.5px;font-weight:600;color:var(--white);line-height:13px}
.band-sub{left:65px;top:69px;font-size:7px;color:#ddd}

/* services */
.svc-head{left:0;width:526px;top:739px;text-align:center}
.svc-head small{font-size:5.5px;color:#555;display:block}
.svc-head h2{font-size:9.5px;font-weight:600;margin-top:2px}
.card{position:absolute;top:780px;width:125px;height:174px;background:var(--white);box-shadow:0 1px 4px rgba(0,0,0,.15);text-align:center}
.card .img{height:81px}
.card h3{font-size:9px;font-weight:600;margin-top:12px}
.card p{font-size:4.2px;line-height:8px;color:#666;margin:5px 10px 0}

/* cta */
.cta{left:66px;top:988px;width:394px;height:149px;overflow:hidden;background:linear-gradient(90deg,#d68a1c,#f29a2a 45%,#f47b20)}
.cta h2{position:absolute;left:16px;top:38px;width:130px;text-align:center;font-size:13px;font-weight:700;line-height:17px;color:#3a2508}

/* contact */
.contact-photo{left:0;top:1178px;width:526px;height:170px;background:
  radial-gradient(ellipse 60px 80px at 100px 90px,rgba(60,45,40,.75),transparent 70%),
  radial-gradient(ellipse 50px 70px at 200px 100px,rgba(90,60,55,.7),transparent 70%),
  linear-gradient(90deg,#ececef 0%,#cfc6c6 40%,#e8e6ea 100%)}
.form{left:247px;top:1178px;width:213px;height:170px;background:linear-gradient(135deg,var(--amber),var(--orange))}
.form h3{position:absolute;left:9px;top:13px;font-size:9px;font-weight:600;color:#2a1a08}
.field{position:absolute;left:6px;width:201px;background:var(--white);border-radius:8px;font-size:4.5px;color:#999;padding:4px 10px}
.send{position:absolute;left:6px;top:147px;width:46px;height:13px;border-radius:8px;background:#1c1c24;color:var(--white);font-size:5px;display:flex;align-items:center;justify-content:center}

/* footer */
.footer{left:0;top:1348px;width:526px;height:152px;background:var(--footer);color:#ccc}
.footer .brand{color:var(--white);left:65px;top:27px}
.socials{left:67px;top:50px;display:flex;gap:5px}
.socials span{width:12px;height:12px;border-radius:50%;border:1px solid #999}
.f-info{left:69px;top:72px;font-size:4px;line-height:10px;color:#ddd}
.f-info div{display:flex;align-items:center;gap:4px}
.f-info i{width:4px;height:4px;border-radius:50%;background:var(--orange);display:inline-block}
.f-h{font-size:5.5px;font-weight:700;color:var(--white)}
.links{left:225px;top:38px;font-size:4px;line-height:12px;color:#bbb}
.gallery{left:323px;top:42px;display:grid;grid-template-columns:repeat(3,34px);gap:5px}
.gallery span{height:33px;display:block}
.copy{left:0;width:526px;text-align:center;font-size:3.8px;color:#aaa}
</style>
</head>
<body>
<div class="stage">
<div class="page">

  <!-- hero -->
  <div class="abs hero-photo" role="img" aria-label="Photo of friends celebrating with champagne and sparklers"></div>
  <svg class="abs" style="left:0;top:0" width="526" height="110" viewBox="0 0 526 110">
    <path d="M0 0H526V8C420 22 330 60 220 78C140 90 60 82 0 76Z" fill="#fff"/>
    <path d="M0 76C60 82 140 90 220 78C330 60 420 22 526 8V16C420 36 330 74 220 90C140 100 60 94 0 90Z" fill="#f47b20"/>
    <path d="M0 90C60 94 140 100 220 90C330 74 420 36 526 16V20C420 42 330 80 220 95C140 104 60 99 0 95Z" fill="#2a2a2a" opacity=".6"/>
  </svg>
  <div class="abs brand">DANA RUTH OKONKWO EVENT DESIGN</div>
  <div class="abs call" style="left:177px"><small>CALL US</small><span>415-555-0193</span></div>
  <nav class="abs nav"><a>HOME</a><a>ABOUT</a><a>SERVICES</a><a>EVENTS</a><a>CONTACT</a><span class="pill">GET STARTED</span></nav>
  <div class="abs hero-text"><div class="l1">ONE STOP</div><div class="l2">EVENT PLANNER</div></div>
  <div class="btn btn-solid" style="left:217px;top:231px;width:42px;height:11px">GET STARTED</div>
  <div class="btn btn-line" style="left:265px;top:231px;width:45px;height:11px">ABOUT US</div>
  <svg class="abs" style="left:0;top:320px" width="526" height="42" viewBox="0 0 526 42">
    <path d="M0 28C80 14 160 34 263 22C360 12 440 32 526 18V42H0Z" fill="#f5f5f5"/>
  </svg>

  <!-- welcome -->
  <section class="abs welcome">
    <div class="abs w-kicker">Welcome To</div>
    <div class="abs w-title">Dana Ruth Okonkwo Event Design</div>
    <p class="abs w-copy">We shape every gathering around the people in it, from the first idea to the last dance. Our team handles venues, vendors, décor and timing so you can simply enjoy the day. Weddings, meetings, fundraisers and parties all get the same care, detail and warm welcome for every guest who walks through the door.</p>
    <div class="btn btn-solid" style="left:65px;top:124px;width:44px;height:12px">GET STARTED</div>
    <div class="abs features">
      <div class="feature"><svg viewBox="0 0 20 20" fill="none" stroke="#f47b20" stroke-width="1.2"><circle cx="10" cy="7" r="3"/><path d="M4 17c0-4 3-6 6-6s6 2 6 6"/></svg><h4>Experienced Team</h4><p>Aliquam vehicula sodales dignissim.</p></div>
      <div class="feature"><svg viewBox="0 0 20 20" fill="none" stroke="#f47b20" stroke-width="1.2"><circle cx="10" cy="8" r="5"/><path d="M8 14h4M8 17h4"/></svg><h4>Brilliant Ideas</h4><p>Aliquam vehicula sodales dignissim.</p></div>
      <div class="feature"><svg viewBox="0 0 20 20" fill="none" stroke="#f47b20" stroke-width="1.2"><circle cx="10" cy="10" r="7"/><path d="M10 6v4l3 2"/></svg><h4>24/7 Suport</h4><p>Aliquam vehicula sodales dignissim.</p></div>
      <div class="feature"><svg viewBox="0 0 20 20" fill="none" stroke="#f47b20" stroke-width="1.2"><circle cx="10" cy="8" r="5"/><path d="M10 5v6M8 7h3M4 17h12"/></svg><h4>Cost Effective</h4><p>Aliquam vehicula sodales dignissim.</p></div>
    </div>
  </section>

  <!-- video band -->
  <section class="abs band">
    <div class="abs band-photo" role="img" aria-label="Photo of a bride and groom in a rustic barn venue"></div>
    <svg class="abs" style="left:0;top:0" width="526" height="148" viewBox="0 0 526 148">
      <path d="M0 0H150C190 60 200 120 0 129Z" fill="#1f1f28" opacity=".75"/>
      <path d="M150 0C210 70 260 140 350 142C420 144 480 112 526 82V96C470 128 420 150 350 148C250 146 200 80 150 0Z" fill="#f47b20"/>
      <circle cx="350" cy="65" r="20" fill="none" stroke="#fff" stroke-width="2"/>
      <path d="M344 54L361 65L344 76Z" fill="none" stroke="#fff" stroke-width="2"/>
    </svg>
    <div class="abs band-title">We Plan and Deliver<br>Event Services</div>
    <div class="abs band-sub">To meet your expectations</div>
    <div class="btn btn-line" style="left:65px;top:84px;width:45px;height:12px">GET STARTED</div>
  </section>

  <!-- services -->
  <div class="abs svc-head"><small>Know About Our</small><h2>Event Design Services</h2></div>
  <div class="card" style="left:66px"><div class="img" role="img" aria-label="Photo of a couple under glowing string lights" style="background:radial-gradient(ellipse 40px 35px at 60px 45px,rgba(220,160,90,.6),transparent 70%),linear-gradient(135deg,#2a3a22,#6a5a32 60%,#3a2a1a)"></div><h3>Weddings</h3><p>Phasellus sollicitudin sapien vel risus laoreet rutrum. Nullam pharetra purus dolor. Pellentesque fringilla purus ut tristique ultrices.</p><div class="btn btn-line-dark" style="left:40px;top:143px;width:45px;height:12px">Get Started</div></div>
  <div class="card" style="left:201px"><div class="img" role="img" aria-label="Photo of colleagues at a corporate meeting" style="background:radial-gradient(ellipse 50px 30px at 60px 40px,rgba(200,180,170,.45),transparent 70%),linear-gradient(135deg,#1e2a40,#4a5a78 60%,#8a9ab0)"></div><h3>Corporate Meetings</h3><p>Phasellus sollicitudin sapien vel risus laoreet rutrum. Nullam pharetra purus dolor. Pellentesque fringilla purus ut tristique ultrices.</p><div class="btn btn-line-dark" style="left:40px;top:143px;width:45px;height:12px">Get Started</div></div>
  <div class="card" style="left:335px"><div class="img" role="img" aria-label="Photo of a family birthday celebration" style="background:radial-gradient(ellipse 40px 30px at 60px 55px,rgba(230,180,200,.6),transparent 70%),linear-gradient(135deg,#7a9a6a,#b4a8a0 55%,#6a7aa0)"></div><h3>Special Events</h3><p>Phasellus sollicitudin sapien vel risus laoreet rutrum. Nullam pharetra purus dolor. Pellentesque fringilla purus ut tristique ultrices.</p><div class="btn btn-line-dark" style="left:40px;top:143px;width:45px;height:12px">Get Started</div></div>

  <!-- call to action -->
  <section class="abs cta">
    <svg class="abs" style="left:0;top:0" width="394" height="149" viewBox="0 0 394 149">
      <defs>
        <radialGradient id="partyGlow" cx="0.7" cy="0.5" r="0.6"><stop offset="0" stop-color="#a0367a"/><stop offset="1" stop-color="#2a1838"/></radialGradient>
      </defs>
      <path d="M235 0H394V149H355C300 100 280 40 235 0Z" fill="url(#partyGlow)" role="img" aria-label="Photo of a lively party with confetti"/>
      <path d="M110 0H235C280 40 300 100 355 149H335C290 110 230 30 180 8Z" fill="#111"/>
      <path d="M225 0H245C285 40 300 100 365 149H345C290 100 265 40 225 0Z" fill="#fff"/>
      <circle cx="198" cy="44" r="41" fill="#111"/><circle cx="198" cy="44" r="36" fill="#6e4a5a" role="img" aria-label="Photo of friends dancing"/>
      <circle cx="293" cy="36" r="34" fill="#fff"/><circle cx="293" cy="36" r="30" fill="#c8a07a" role="img" aria-label="Photo of a birthday party"/>
      <circle cx="288" cy="117" r="27" fill="#111"/><circle cx="288" cy="117" r="22" fill="#8a6a5a" role="img" aria-label="Photo of guests celebrating"/>
    </svg>
    <h2>ARE YOU READY TO MAKE YOUR OWN SPECIAL EVENTS?</h2>
    <div class="btn" style="left:40px;top:99px;width:45px;height:11px;border:1px solid #2a1a08;color:#2a1a08">Get Started</div>
  </section>

  <!-- contact -->
  <div class="abs contact-photo" role="img" aria-label="Photo of a laughing couple under falling confetti"></div>
  <section class="abs form">
    <h3>Get In Touch</h3>
    <div class="field" style="top:33px;height:15px">Name</div>
    <div class="field" style="top:56px;height:15px">E-mail</div>
    <div class="field" style="top:80px;height:58px">Message</div>
    <div class="send">SEND</div>
  </section>

  <!-- footer -->
  <footer class="abs footer">
    <div class="abs brand">DANA RUTH OKONKWO EVENT DESIGN</div>
    <div class="abs socials"><span></span><span></span><span></span><span></span></div>
    <div class="abs f-info">
      <div><i></i>Bayview Harbor Rowing Club</div>
      <div><i></i>415-555-0193</div>
      <div><i></i>droeventstudio@vesperlane.com</div>
    </div>
    <div class="abs f-h" style="left:225px;top:27px">QUICK LINKS</div>
    <div class="abs links">Home<br>About<br>Services<br>Events<br>Contact</div>
    <div class="abs f-h" style="left:322px;top:27px">PICTURE GALLERY</div>
    <div class="abs gallery">
      <span role="img" aria-label="Party photo" style="background:linear-gradient(135deg,#d08a8a,#8a3a4a)"></span>
      <span role="img" aria-label="Party photo" style="background:linear-gradient(135deg,#7a6ac0,#3a2a7a)"></span>
      <span role="img" aria-label="Party photo" style="background:linear-gradient(135deg,#6a4a8a,#2a1a3a)"></span>
      <span role="img" aria-label="Party photo" style="background:linear-gradient(135deg,#9a5a7a,#3a2a4a)"></span>
      <span role="img" aria-label="Party photo" style="background:linear-gradient(135deg,#9a9ab8,#3a3a5a)"></span>
      <span role="img" aria-label="Party photo" style="background:linear-gradient(135deg,#9a7a5a,#4a3a2a)"></span>
    </div>
    <div class="abs copy" style="top:141px">© Dana Ruth Okonkwo Event Design, All Rights Reserved. Privacy Policy</div>
  </footer>

</div>
</div>
</body>
</html>
```